Build a new template and redesign the existing deck

We need a designer to build a customer template using color scheme from our website - www.quellor.io. Then, we need the designer to redesign the existing document - attached - into the new template.

```html
<!DOCTYPE html>
<html lang="en">
<head>
<meta charset="utf-8">
<title>quellor</title>
<link href="https://fonts.googleapis.com/css2?family=EB+Garamond:wght@400;500&family=Rubik:wght@400;500;700&family=Lora:wght@400;600&display=swap" rel="stylesheet">
<style>
:root{
  --navy-deep:#06104f;
  --navy:#0c2382;
  --accent:#5aaed8;
  --ink:#1d1d1f;
  --muted:#555a63;
  --tick:#b7b86a;
  --mist:#eef2f8;
  --sand:#ede8c6;
  --lilac:#a9abd6;
  --white:#ffffff;
  --serif:'EB Garamond', Georgia, serif;
  --sans:'Rubik', Arial, sans-serif;
}
*{margin:0;padding:0;box-sizing:border-box}
html,body{width:1200px;height:4357px;overflow:hidden}
body{position:relative;background:var(--white);font-family:var(--sans);color:var(--ink)}
.abs{position:absolute}
section{position:absolute;left:0;width:1200px;overflow:hidden}

.hero{top:0;height:738px;background:radial-gradient(ellipse at 80% 30%,#1a3fb0 0%,var(--navy) 40%,var(--navy-deep) 100%)}
.hero-waves{position:absolute;left:0;bottom:0;width:1200px;height:420px;background:linear-gradient(170deg,rgba(80,150,240,0) 30%,rgba(80,160,240,.28) 60%,rgba(40,90,200,.1) 100%)}
.brand-xl{font-family:var(--sans);font-weight:400;color:var(--white);font-size:92px;line-height:1;left:142px;top:56px}
.section-title{font-family:var(--sans);font-weight:700;color:var(--accent);font-size:39px;letter-spacing:1px;line-height:48px;text-transform:uppercase}
.hero .section-title{left:144px;top:312px}
.vision{left:147px;top:386px;color:var(--white);font-size:17px;line-height:32px}

.brand-sm{font-family:var(--sans);font-weight:400;color:var(--ink);font-size:34px;line-height:1}

.challenges{top:738px;height:1471px;background:var(--white)}
.challenges .section-title{left:142px;top:72px}
.challenges .brand-sm{left:921px;top:80px}
.point{width:470px;font-size:18.5px;line-height:34px;color:var(--muted)}
.point strong{display:block;color:var(--ink);font-weight:500;font-size:18px;line-height:28px;white-space:nowrap}
.point svg{position:absolute;left:-40px;top:4px}
.news{background:var(--white);box-shadow:0 0 6px rgba(0,0,0,.25);overflow:hidden}
.news-bar{height:56px;background:#111;color:var(--white);display:flex;align-items:center;padding:0 16px;gap:14px;font-weight:700}
.news-body{padding:16px 14px}
.headline{font-weight:700;font-size:28px;line-height:36px}
.byline{font-size:12px;color:var(--muted);margin-top:6px}
.tag{display:inline-block;font-size:11px;color:var(--white);padding:1px 6px;margin-right:4px}
.dot{display:inline-block;width:42px;height:42px;border-radius:50%;background:#35589f;margin-right:6px}
.footnotes{left:142px;top:1272px;font-size:19.5px;line-height:34px;color:var(--ink)}

.problem{top:2209px;height:668px;background:linear-gradient(180deg,#d7dde6 0%,var(--mist) 35%,#e6edf6 70%,#dfe6ef 100%)}
.problem .section-title{left:142px;top:206px}
.problem .brand-sm{left:877px;top:214px;font-size:42px}
.problem-lines{left:142px;top:296px;font-size:17px;line-height:42px;color:var(--muted)}
.problem-lines strong{color:var(--ink);font-weight:700}

.solution{top:2877px;height:733px;background:#fafbfd}
.solution .section-title{left:142px;top:104px}
.solution .brand-sm{left:921px;top:112px}
.solution-lead{left:142px;top:196px;font-size:27px;font-weight:500;line-height:40px}
.pillar{width:330px;text-align:center;top:350px}
.pillar .disc{width:176px;height:176px;border-radius:50%;margin:0 auto;display:flex;align-items:center;justify-content:center}
.pillar h3{font-size:19px;font-weight:500;letter-spacing:.5px;margin-top:30px}
.pillar p{font-family:var(--serif);font-size:17px;color:var(--muted);margin-top:10px}

.closing{top:3610px;height:747px;background:linear-gradient(180deg,#eaf1fa 0%,#f3f6fb 60%,#eef1f8 100%)}
.closing-waves{position:absolute;left:0;bottom:0;width:1200px;height:360px;background:linear-gradient(100deg,rgba(240,160,190,.35) 0%,rgba(245,225,150,.35) 25%,rgba(170,200,240,.25) 55%,rgba(190,170,230,.35) 75%,rgba(140,220,200,.35) 100%);-webkit-mask:linear-gradient(180deg,transparent 0%,#000 70%);mask:linear-gradient(180deg,transparent 0%,#000 70%)}
.brand-hero{left:0;width:1200px;text-align:center;top:110px;font-family:var(--sans);font-weight:400;font-size:160px;line-height:1;color:var(--ink)}
.page-no{right:24px;bottom:10px;font-family:var(--serif);font-size:11px;color:var(--muted)}
</style>
</head>
<body>

<section class="hero">
  <div class="hero-waves" role="img" aria-label="Flowing blue line-wave pattern"></div>
  <div class="abs brand-xl">quellor</div>
  <h2 class="abs section-title">Vision Statement</h2>
  <p class="abs vision">Easy to use, quellor is the go-to solution for private and secure communications.<br>We are the Payvia of data transfer privacy and security.<br>Make the Internet secure again.</p>
</section>

<section class="challenges">
  <h2 class="abs section-title">Privacy and Security<br>Challenges have grown<br>in importance</h2>
  <div class="abs brand-sm">quellor</div>

  <div class="abs point" style="left:181px;top:278px">
    <svg width="24" height="24" viewBox="0 0 24 24"><circle cx="12" cy="12" r="12" fill="var(--tick)"/><path d="M7 12.5l3.2 3.2L17 9" stroke="#fff" stroke-width="2.4" fill="none"/></svg>
    <strong>Customers demand high standards</strong>for data security and privacy</div>
  <div class="abs point" style="left:621px;top:278px">
    <svg width="24" height="24" viewBox="0 0 24 24"><circle cx="12" cy="12" r="12" fill="var(--tick)"/><path d="M7 12.5l3.2 3.2L17 9" stroke="#fff" stroke-width="2.4" fill="none"/></svg>
    <strong>Regulators have introduced mandates</strong>for data security and privacy<br>(e.g., GDPR Article 25, CCPA 1798.140/d/g)</div>
  <div class="abs point" style="left:181px;top:396px">
    <svg width="24" height="24" viewBox="0 0 24 24"><circle cx="12" cy="12" r="12" fill="var(--tick)"/><path d="M7 12.5l3.2 3.2L17 9" stroke="#fff" stroke-width="2.4" fill="none"/></svg>
    <strong>Companies do not have solutions<br>nor resources</strong>to address challenges in their environments</div>
  <div class="abs point" style="left:621px;top:422px">
    <svg width="24" height="24" viewBox="0 0 24 24"><circle cx="12" cy="12" r="12" fill="var(--tick)"/><path d="M7 12.5l3.2 3.2L17 9" stroke="#fff" stroke-width="2.4" fill="none"/></svg>
    <strong>Privacy and security incidents continue to grow</strong>in number and in total estimated damages</div>

  <article class="abs news" style="left:154px;top:565px;width:425px;height:310px">
    <div class="news-bar" style="background:#1a1a1a;font-size:28px">Ledger Wire</div>
    <div class="news-body">
      <div class="headline" style="font-size:26px;line-height:34px">A hacker gained access to 100 million Harbor Bank credit card applications and accounts</div>
      <div class="byline">By Alan Pryce, Ledger Wire</div>
      <div class="byline">Updated 5:17 PM EDT, Tue July 30, 2019</div>
      <div style="margin-top:8px"><span class="dot"></span><span class="dot" style="background:#4aa3e6"></span></div>
    </div>
  </article>

  <article class="abs news" style="left:615px;top:565px;width:422px;height:305px">
    <div class="news-bar" style="background:#222;font-size:24px">Privacy Desk</div>
    <div class="news-body" style="text-align:center">
      <div><span class="tag" style="background:#d46a2a">CYBER SECURITY</span><span class="tag" style="background:#9a2a22">NEWS</span><span style="font-size:11px">6 MIN READ</span></div>
      <div style="font-size:23px;line-height:30px;margin-top:14px">Vitalink Labs Data Breach, the Largest Ever in Canada, May Cost the Company over $1 Billion in Class-Action Lawsuit</div>
      <div style="font-size:12px;margin-top:22px">DANA MOREAU | JANUARY 8, 2020</div>
    </div>
  </article>

  <article class="abs news" style="left:158px;top:912px;width:425px;height:305px">
    <div class="news-bar" style="background:#111;font-family:'Lora',Georgia,serif;font-size:30px">Meridian</div>
    <div class="news-body" style="font-family:'Lora',Georgia,serif">
      <div style="font-size:10px;color:var(--muted)">EDITORS' PICK | 226,363 views | Jan 22, 2020, 6:10 am EST</div>
      <div style="font-size:25px;line-height:36px;margin-top:8px">Northgate Software Security Shocker As 250 Million Customer Records Exposed Online</div>
      <div style="font-family:var(--sans);font-size:13px;margin-top:8px"><b>Karl Ostrow</b> <span style="color:var(--muted)">Senior Contributor</span></div>
      <div style="font-family:var(--sans);font-size:12px;color:#2b6cc4;margin-top:2px">Cybersecurity</div>
      <div style="font-size:11px;font-style:italic;color:var(--muted);margin-top:4px">I report and analyse breaking cybersecurity and privacy stories</div>
    </div>
  </article>

  <article class="abs news" style="left:620px;top:912px;width:420px;height:305px">
    <div class="news-bar" style="background:#000;font-size:22px;justify-content:space-between"><span>Tallis News</span><span style="font-size:18px">Subscribe</span></div>
    <div class="news-body">
      <div style="font-size:15px">Technology</div>
      <div class="headline" style="font-size:34px;line-height:37px;letter-spacing:-.5px;margin-top:4px">Confero Sued for Fraud Over Privacy, Security Flaws</div>
      <div style="font-size:12px;margin-top:10px">By Nina Halvers</div>
      <div style="font-size:12px">April 8, 2020, 12:15 AM EDT</div>
      <div style="font-size:12px;font-style:italic">Updated on April 8, 2020, 2:11 AM EDT</div>
      <div style="border-top:1px dashed #777;margin-top:10px;padding-top:4px;font-size:16px">&#9656; The lawsuit comes after agencies ban the</div>
    </div>
  </article>

  <ol class="abs footnotes" style="list-style:none">
    <li>1. Corvane estimated that 11.7B records leaked over the past three years alone (2019)</li>
    <li>2. Atlas Bank projected the number of cybersecurity incidents to increase by 20-30% per year (2019)</li>
    <li>3. National Crypto Office shared findings on multiple cryptography algorithms compromised (2018)</li>
  </ol>
</section>

<section class="problem" role="img" aria-label="Soft grey-blue halftone dot texture">
  <h2 class="abs section-title">Problem Statement</h2>
  <div class="abs brand-sm">quellor</div>
  <p class="abs problem-lines"><strong>User data is vulnerable</strong> during transmission over public domain.<br><strong>Trust is bestowed</strong> on companies to protect their consumers' data.<br><strong>No easy way exists</strong> to build software with security and privacy in mind.</p>
</section>

<section class="solution">
  <h2 class="abs section-title">Solution</h2>
  <div class="abs brand-sm">quellor</div>
  <p class="abs solution-lead">Technology stack for easy implementation of privacy<br>and security for data transfer</p>

  <div class="abs pillar" style="left:104px">
    <div class="disc" style="background:var(--sand)">
      <svg width="90" height="90" viewBox="0 0 90 90" fill="none" stroke="#fff" stroke-width="4"><circle cx="45" cy="34" r="10"/><circle cx="45" cy="34" r="20" stroke-dasharray="8 6"/><path d="M12 62h18l12 6h20l14-10"/><path d="M12 74h22l14 4 28-14"/></svg>
    </div>
    <h3>TECHNOLOGY PLATFORM</h3><p>for system privacy</p>
  </div>
  <div class="abs pillar" style="left:437px">
    <div class="disc" style="background:var(--accent)">
      <svg width="90" height="90" viewBox="0 0 90 90" fill="none" stroke="#fff" stroke-width="4"><path d="M45 8l30 10v24c0 20-14 32-30 40C29 74 15 62 15 42V18z"/><rect x="31" y="40" width="28" height="22" rx="3" fill="#fff"/><path d="M36 40v-6a9 9 0 0118 0v6"/><circle cx="45" cy="50" r="3" fill="var(--accent)" stroke="none"/></svg>
    </div>
    <h3>SECURITY-AS-A-SERVICE</h3><p>for data protection</p>
  </div>
  <div class="abs pillar" style="left:771px">
    <div class="disc" style="background:var(--lilac)">
      <svg width="110" height="90" viewBox="0 0 110 90" fill="none" stroke="#fff" stroke-width="4" stroke-linejoin="round"><path d="M8 32l22-20v12h44v16H30v12z"/><path d="M102 58L80 38v12H36v16h44v12z"/></svg>
    </div>
    <h3>END-TO-END TRANSFER</h3><p>for data security</p>
  </div>
</section>

<section class="closing">
  <div class="closing-waves" role="img" aria-label="Pastel rainbow line-wave pattern"></div>
  <div class="abs brand-hero">quellor</div>
  <div class="abs page-no">C9</div>
</section>

</body>
</html>
```